Lawn Sign For Construction Projects - Brisk Current

This contest is for a lawn sign that will be placed in the front yard of recently completed construction projects. The goal here is to have a bold advertising sign that is visible from a vehicle driving past.

We are still deciding on the default size for our sign, we also may use multiple sizes. The two sizes we will more than likely be using are: 18"h x 24"w and 24"h x 36"w.

Preference will be given to designers that submit original designs that tie into our current brand and are either in both the size formats listed above or are easy to scale in photoshop or illustrator.

In the files, you will see our logo and an example of a lawn sign.

Please contact us with any questions or comments you may have!

Thank You,
- The Brisk Current Team

Industry/Entity Type

Residential Construction

Colors
34a7d8
ffffff
faa54b

Requirements
Nice to have
• 1. The sign must tie into our current branding and color scheme.
• 2. The sign must be clearly visible and readable.
• 3. The sign must include our phone number in readable print.
• 4. Our website written in small print along the bottom of the sign.
• 5. Must mention we install the following products:
• a.) Solar
• b.) Roofing
• c.) Windows
• d.) Artificial Lawn
• e.) Whole House Fans
• f.) Patio Covers

```html
<!DOCTYPE html>
<html lang="en">
<head>
<meta charset="utf-8">
<title>Brisk Current – Lawn Sign</title>
<link rel="stylesheet" href="https://fonts.googleapis.com/css2?family=Cinzel:wght@600&family=Montserrat:wght@600;700&display=swap">
<style>
  :root {
    --cream: #fcfbe3;
    --leaf: #a6cd47;
    --leaf-light: #c3dc6a;
    --lime-pale: #e6ec9c;
    --band: #86b82f;
    --band-text: #f6f4b8;
    --brand-blue: #34a7d8;
    --brand-orange: #faa54b;
    --ink: #2f2f2f;
    --white: #ffffff;
    --mint: #a9e3cf;
    --mint-soft: #e4efb8;
  }
  html, body {
    margin: 0;
    padding: 0;
    width: 1200px;
    height: 900px;
    overflow: hidden;
    background: var(--cream);
  }
  .sign {
    position: relative;
    width: 1200px;
    height: 900px;
    overflow: hidden;
    background: var(--cream);
  }
  .scenery { position: absolute; inset: 0; }
  .services-text {
    font-family: "Cinzel", serif;
    font-weight: 600;
    font-size: 31px;
    fill: var(--band-text);
    letter-spacing: 1px;
  }
  .sun {
    position: absolute;
    left: 60px; top: 30px;
    width: 140px; height: 140px;
    border-radius: 50%;
    background: radial-gradient(circle, #ffffff 0%, #fffbe0 45%, rgba(255,255,255,0) 72%);
  }
  .cloud {
    position: absolute;
    background: var(--white);
    border-radius: 40px;
    opacity: 0.95;
  }
  .cloud--a { left: 515px; top: 10px;  width: 96px; height: 58px; }
  .cloud--b { left: 245px; top: 118px; width: 86px; height: 50px; }
  .cloud--c { left: 465px; top: 162px; width: 56px; height: 34px; }
  .cloud--d { left: 118px; top: 250px; width: 62px; height: 38px; }
  .butterflies {
    position: absolute;
    left: 760px; top: 400px;
    width: 420px; height: 400px;
    background:
      radial-gradient(ellipse 90px 80px at 120px 110px, var(--mint) 0 98%, transparent 100%),
      radial-gradient(ellipse 40px 35px at 270px 180px, var(--mint-soft) 0 98%, transparent 100%),
      radial-gradient(ellipse 30px 26px at 270px 330px, var(--mint-soft) 0 98%, transparent 100%),
      radial-gradient(ellipse 30px 26px at 395px 355px, var(--mint-soft) 0 98%, transparent 100%);
    opacity: 0.85;
  }
  .grass {
    position: absolute;
    left: 0; right: 0; bottom: 0;
    height: 180px;
    background: linear-gradient(to bottom, rgba(140,200,60,0) 0%, #8cc83c 22%, #5aa52a 60%, #3f8a1f 100%);
  }
  .brand {
    position: absolute;
    left: 58px;
    top: 470px;
    width: 360px;
    text-align: center;
    font-family: "Montserrat", sans-serif;
  }
  .brand__dot {
    width: 100px; height: 100px;
    margin: 0 auto 18px;
    border-radius: 50%;
    background: var(--brand-orange);
  }
  .brand__name {
    margin: 0;
    font-size: 50px;
    font-weight: 700;
    color: var(--brand-blue);
    letter-spacing: 0.5px;
    text-transform: uppercase;
    line-height: 1;
    white-space: nowrap;
  }
  .brand__phone {
    margin: 14px 0 0;
    font-size: 40px;
    font-weight: 600;
    color: var(--ink);
    letter-spacing: 4px;
    line-height: 1;
  }
  .website {
    position: absolute;
    right: 52px;
    bottom: 12px;
    margin: 0;
    font-family: "Montserrat", sans-serif;
    font-weight: 700;
    font-size: 22px;
    color: var(--white);
    letter-spacing: 1px;
    text-transform: uppercase;
  }
</style>
</head>
<body>
<main class="sign">
  <svg class="scenery" width="1200" height="900" viewBox="0 0 1200 900" aria-hidden="false">
    <rect class="backdrop" width="1200" height="900" fill="var(--cream)"/>
    <path class="hill-main" d="M0,0 H1200 V470 C900,385 400,365 0,440 Z" fill="var(--leaf)"/>
    <path class="hill-light" d="M0,0 H1200 V250 C850,165 400,180 0,300 Z" fill="var(--leaf-light)"/>
    <path class="hill-pale" d="M560,0 H1200 V120 C1000,60 800,30 560,0 Z" fill="var(--lime-pale)"/>
    <path class="service-band" d="M0,330 C350,230 850,230 1200,300 L1200,445 C850,350 350,345 0,432 Z" fill="var(--band)"/>
    <defs>
      <path id="service-curve" d="M18,392 C380,298 820,298 1182,398"/>
    </defs>
    <text class="services-text">
      <textPath href="#service-curve" startOffset="0" textLength="1160" lengthAdjust="spacing">Solar | Roofing | Windows | Artificial Lawn | Whole House Fans | Patio Covers</textPath>
    </text>
  </svg>

  <div class="sun" role="img" aria-label="Bright sun illustration"></div>
  <div class="cloud cloud--a" role="img" aria-label="Small cloud illustration"></div>
  <div class="cloud cloud--b" role="img" aria-label="Small cloud illustration"></div>
  <div class="cloud cloud--c" role="img" aria-label="Small cloud illustration"></div>
  <div class="cloud cloud--d" role="img" aria-label="Small cloud illustration"></div>
  <div class="butterflies" role="img" aria-label="Pale mint butterflies fluttering"></div>
  <div class="grass" role="img" aria-label="Fresh green grass along the bottom edge"></div>

  <section class="brand">
    <div class="brand__dot"></div>
    <h1 class="brand__name">Brisk Current</h1>
    <p class="brand__phone">0800-555-0199</p>
  </section>

  <p class="website">www.briskcurrent.com</p>
</main>
</body>
</html>
```